Creative Design "Size Chart" for a Clothing Product

Hi, My dear friends! I am looking to do a contest to design a unique creative "Size Chart" for our clothing line. See Attached the Sizes & Ideas Thanks Good Luck Osvald

Colors

Designer to choose colors to be used in the design.

```html
<!DOCTYPE html>
<html lang="en">
<head>
<meta charset="utf-8">
<title>Size Chart</title>
<link rel="stylesheet" href="https://fonts.googleapis.com/css2?family=Barlow+Semi+Condensed:wght@400;600;700&display=swap">
<style>
  :root {
    --ink: #111;
    --white: #fff;
    --men-title: #2f5796; --men-head: #7b89b9;
    --men-1: #b1b8d7; --men-2: #bcc1de; --men-3: #c8cce4; --men-4: #d3d6ea; --men-5: #e0e2f0; --men-6: #eceef6;
    --men-fig-top: #2f5796; --men-fig-bottom: #bde3f2;
    --women-title: #ee1657; --women-head: #ef5a6f;
    --women-1: #f8b3b6; --women-2: #f9bfc1; --women-3: #fac8c9; --women-4: #fbd2d2; --women-5: #fcdcdc; --women-6: #fce6e5; --women-7: #fdf0ee;
    --women-fig-top: #ee1f55; --women-fig-bottom: #f7c3c8;
    --boys-title: #0089d0; --boys-head: #38a2da;
    --boys-1: #aacdeb; --boys-2: #b8d5ef; --boys-3: #c5dcf1; --boys-4: #d2e3f4; --boys-5: #dfeaf7; --boys-6: #ebf3fb;
    --boys-fig-top: #0089d0; --boys-fig-bottom: #a8cbec;
    --girls-title: #ec008c; --girls-head: #f186b5;
    --girls-1: #f5b6d0; --girls-2: #f7c1d7; --girls-3: #f8cadd; --girls-4: #f9d3e3; --girls-5: #fadce9; --girls-6: #fce8f1;
    --girls-fig-top: #ec008c; --girls-fig-bottom: #f9d5e7;
  }
  * { margin: 0; padding: 0; box-sizing: border-box; }
  html, body { width: 927px; height: 1200px; overflow: hidden; background: var(--white); }
  body { position: relative; font-family: "Barlow Semi Condensed", sans-serif; color: var(--ink); }

  .figure { position: absolute; border-radius: 46% 46% 12% 12% / 14% 14% 4% 4%; }
  .men .figure   { left: 257px; top: 82px;  width: 130px; height: 215px; background: linear-gradient(var(--men-fig-top), var(--men-fig-bottom)); }
  .women .figure { left: 276px; top: 335px; width: 93px;  height: 240px; background: linear-gradient(var(--women-fig-top), var(--women-fig-bottom)); }
  .boys .figure  { left: 276px; top: 615px; width: 92px;  height: 214px; background: linear-gradient(var(--boys-fig-top), var(--boys-fig-bottom)); }
  .girls .figure { left: 284px; top: 869px; width: 84px;  height: 214px; background: linear-gradient(var(--girls-fig-top), var(--girls-fig-bottom)); }

  .measure { position: absolute; left: 212px; font-weight: 600; font-size: 15px; line-height: 1; border-bottom: 1px dotted var(--ink); padding-bottom: 3px; }

  .chart { position: absolute; left: 417px; width: 284px; }
  .chart-title { height: 25.5px; line-height: 25.5px; text-align: center; color: var(--white); font-size: 15px; margin-bottom: 11.5px; }
  .men .chart-title, .women .chart-title { font-weight: 700; }
  .row { display: flex; height: 25.4px; line-height: 25.4px; font-size: 15px; }
  .row span { flex: 1; text-align: center; }
  .row span:first-child { font-weight: 700; }
  .row.head { color: var(--white); font-weight: 700; height: 25.5px; }
  .row.head span { font-weight: 700; }

  .men .chart { top: 82px; }   .men .chart-title { background: var(--men-title); } .men .head { background: var(--men-head); }
  .men .r1{background:var(--men-1)} .men .r2{background:var(--men-2)} .men .r3{background:var(--men-3)}
  .men .r4{background:var(--men-4)} .men .r5{background:var(--men-5)} .men .r6{background:var(--men-6)}

  .women .chart { top: 336px; } .women .chart-title { background: var(--women-title); } .women .head { background: var(--women-head); }
  .women .r1{background:var(--women-1)} .women .r2{background:var(--women-2)} .women .r3{background:var(--women-3)}
  .women .r4{background:var(--women-4)} .women .r5{background:var(--women-5)} .women .r6{background:var(--women-6)} .women .r7{background:var(--women-7)}

  .boys .chart { top: 615px; } .boys .chart-title { background: var(--boys-title); } .boys .head { background: var(--boys-head); }
  .boys .r1{background:var(--boys-1)} .boys .r2{background:var(--boys-2)} .boys .r3{background:var(--boys-3)}
  .boys .r4{background:var(--boys-4)} .boys .r5{background:var(--boys-5)} .boys .r6{background:var(--boys-6)}

  .girls .chart { top: 869px; } .girls .chart-title { background: var(--girls-title); } .girls .head { background: var(--girls-head); }
  .girls .r1{background:var(--girls-1)} .girls .r2{background:var(--girls-2)} .girls .r3{background:var(--girls-3)}
  .girls .r4{background:var(--girls-4)} .girls .r5{background:var(--girls-5)} .girls .r6{background:var(--girls-6)}
</style>
</head>
<body>

<section class="men">
  <div class="figure" role="img" aria-label="Silhouette of a man showing chest and waist measuring points"></div>
  <div class="measure" style="top:155px;width:145px">CHEST</div>
  <div class="measure" style="top:209px;width:142px">WAIST</div>
  <div class="chart">
    <div class="chart-title">MENS</div>
    <div class="row head"><span>SIZE</span><span>CHEST</span><span>WAIST</span></div>
    <div class="row r1"><span>S</span><span>34-36</span><span>28-30</span></div>
    <div class="row r2"><span>M</span><span>36-38</span><span>30-32</span></div>
    <div class="row r3"><span>L</span><span>38-40</span><span>32-34</span></div>
    <div class="row r4"><span>XL</span><span>40-42</span><span>34-36</span></div>
    <div class="row r5"><span>2X</span><span>43-45</span><span>36-40</span></div>
    <div class="row r6"><span>3X</span><span>45-48</span><span>40-44</span></div>
  </div>
</section>

<section class="women">
  <div class="figure" role="img" aria-label="Silhouette of a woman showing chest and waist measuring points"></div>
  <div class="measure" style="top:410px;width:136px">CHEST</div>
  <div class="measure" style="top:449px;width:132px">WAIST</div>
  <div class="chart">
    <div class="chart-title">WOMENS</div>
    <div class="row head"><span>SIZE</span><span>CHEST</span><span>WAIST</span></div>
    <div class="row r1"><span>XS (0-2)</span><span>32-34</span><span>26-28</span></div>
    <div class="row r2"><span>S (4-6)</span><span>34-36</span><span>28-30</span></div>
    <div class="row r3"><span>M (8-10)</span><span>36-38</span><span>30-32</span></div>
    <div class="row r4"><span>L (12-14)</span><span>38-40</span><span>32-34</span></div>
    <div class="row r5"><span>XL (14-16 )</span><span>40-42</span><span>34-36</span></div>
    <div class="row r6"><span>2X (18)</span><span>42-44</span><span>36-38</span></div>
    <div class="row r7"><span>3X (20)</span><span>44-46</span><span>38-40</span></div>
  </div>
</section>

<section class="boys">
  <div class="figure" role="img" aria-label="Silhouette of a boy showing chest and waist measuring points"></div>
  <div class="measure" style="top:685px;width:134px">CHEST</div>
  <div class="measure" style="top:718px;width:135px">WAIST</div>
  <div class="chart">
    <div class="chart-title">BOYS</div>
    <div class="row head"><span>SIZE</span><span>CHEST</span><span>WAIST</span></div>
    <div class="row r1"><span>XXS</span><span>20-23</span><span>19-21</span></div>
    <div class="row r2"><span>XS</span><span>23-26</span><span>21-23</span></div>
    <div class="row r3"><span>S</span><span>26-29</span><span>32-25</span></div>
    <div class="row r4"><span>M</span><span>29-32</span><span>25-27</span></div>
    <div class="row r5"><span>L</span><span>32-35</span><span>27-29</span></div>
    <div class="row r6"><span>XL</span><span>35-38</span><span>29-31</span></div>
  </div>
</section>

<section class="girls">
  <div class="figure" role="img" aria-label="Silhouette of a girl showing chest and waist measuring points"></div>
  <div class="measure" style="top:939px;width:136px">CHEST</div>
  <div class="measure" style="top:963px;width:134px">WAIST</div>
  <div class="chart">
    <div class="chart-title">GIRLS</div>
    <div class="row head"><span>SIZE</span><span>CHEST</span><span>WAIST</span></div>
    <div class="row r1"><span>XXS</span><span>19-22</span><span>18-20</span></div>
    <div class="row r2"><span>XS</span><span>22-25</span><span>20-22</span></div>
    <div class="row r3"><span>S</span><span>25-28</span><span>22-24</span></div>
    <div class="row r4"><span>M</span><span>28-31</span><span>24-26</span></div>
    <div class="row r5"><span>L</span><span>31-34</span><span>26-28</span></div>
    <div class="row r6"><span>XL</span><span>34-37</span><span>28-30</span></div>
  </div>
</section>

</body>
</html>
```